Tavelin: A Friday night of the Kindled Word Flyer

We are holding 2 Friday night events, one on 10/25/19 and the other on 11/29/19.
The time frame is 6:30pm-9:00pm. These services will be a time of prayer/healing for the sick and will be prophetic as well. (There will be prophets prophesying over people)

The event is called: Tavelin: A Friday night of the Kindled Word
The flyer should also include the phrase/excerpt: "And they prophesied also".

Keywords/Phrases: Prophetic, Healing, Climbing in the Spirit, Higher level of Anointing...

Target Market(s)

those looking for healing, seeking a word from God

Colors

Designer to choose colors to be used in the design.

Requirements
Must have
• The event is called: Tavelin: A Friday night of the Kindled Word
• The flyer should also include the phrase/excerpt: "And they prophesied also".
• It must include the Quorvel logo attached, either is fine, we have attached two different versions.
• It must have the dates, location, time
• Dates: October 25, 2019 and November 29, 2019
• Location: Loftmere Community Center
• (Downtown Portland) 248 Wendlow Street
• Portland, ME 04102
• Time: 6:30pm-9:00pm
• Contact Info: Tel. 207-583-2914
• email: contact@ambervale.example
• web: www.quorvel.example
Nice to have
• creativity in color scheme, the meaning of the word Tavelin conveyed in a classy artistic way/design.
Should not have
• Crosses, pictures of churches

```html
<!DOCTYPE html>
<html lang="en">
<head>
<meta charset="UTF-8">
<title>Tavelin: A Friday Night of the Kindled Word</title>
<link rel="stylesheet" href="https://fonts.googleapis.com/css2?family=Montserrat:wght@700;800;900&family=Barlow+Condensed:wght@500;600;700&family=Dancing+Script:wght@600&display=swap">
<style>
  :root {
    --page-bg: #e9e9e9;
    --flyer-bg: #1f1c1a;
    --ink-white: #ffffff;
    --accent-amber: #f4a11d;
    --accent-red: #d92027;
    --sky-deep: #9c1512;
    --sky-mid: #e8361c;
    --sky-glow: #f7941d;
  }
  * { margin: 0; padding: 0; box-sizing: border-box; }
  html, body {
    width: 1200px; height: 750px; overflow: hidden;
    background: var(--page-bg);
  }
  .flyer {
    position: absolute; left: 330px; top: 28px;
    width: 540px; height: 694px;
    background: var(--flyer-bg);
    overflow: hidden;
    font-family: 'Barlow Condensed', sans-serif;
    color: var(--ink-white);
    text-align: center;
  }
  .sky-artwork {
    position: absolute; left: 0; top: 0; width: 540px; height: 290px;
    background:
      radial-gradient(ellipse 140px 120px at 300px 40px, var(--sky-glow), transparent 80%),
      linear-gradient(180deg, var(--sky-deep) 0%, var(--sky-mid) 45%, #c4261a 75%, var(--flyer-bg) 100%);
  }
  .brand {
    position: absolute; left: 46px; top: 62px;
    display: flex; align-items: center; gap: 8px;
  }
  .brand-dot {
    width: 14px; height: 14px; border-radius: 50%;
    background: var(--accent-amber);
  }
  .brand-name {
    font-family: 'Montserrat', sans-serif; font-weight: 800;
    font-size: 28px; letter-spacing: 1px; color: var(--ink-white);
  }
  .event-title {
    position: absolute; left: 0; right: 0; top: 268px;
    font-family: 'Montserrat', sans-serif; font-weight: 900;
    font-size: 62px; line-height: 1; letter-spacing: -1px;
    color: var(--ink-white);
  }
  .event-subtitle {
    position: absolute; left: 0; right: 0; top: 340px;
    font-family: 'Montserrat', sans-serif; font-weight: 700;
    font-size: 16.5px; letter-spacing: 0.5px;
    color: var(--accent-amber);
  }
  .scripture-band {
    position: absolute; left: 82px; top: 381px;
    width: 378px; height: 48px;
    background: var(--accent-red);
    clip-path: polygon(1% 8%, 30% 0, 70% 4%, 100% 0, 99% 55%, 100% 100%, 60% 96%, 25% 100%, 0 94%, 2% 50%);
    display: flex; align-items: center; justify-content: center;
    font-weight: 700; font-size: 33px; letter-spacing: 0.2px;
  }
  .event-dates {
    position: absolute; left: 0; right: 0; top: 444px;
    font-weight: 600; font-size: 27px;
  }
  .event-dates .joiner {
    font-family: 'Dancing Script', cursive; font-weight: 600;
    color: var(--accent-amber); font-size: 24px; margin: 0 4px;
  }
  .venue-name {
    position: absolute; left: 0; right: 0; top: 488px;
    font-weight: 700; font-size: 38px; color: var(--accent-amber);
  }
  .venue-address {
    position: absolute; left: 0; right: 0; top: 535px;
    font-weight: 500; font-size: 21px; line-height: 25px;
  }
  .event-time {
    position: absolute; left: 143px; top: 600px;
    width: 254px; height: 48px;
    border-top: 2px solid var(--accent-amber);
    border-bottom: 2px solid var(--accent-amber);
    font-weight: 700; font-size: 42px; line-height: 44px;
    color: var(--accent-amber);
  }
  .contact-line {
    position: absolute; left: 0; right: 0; top: 663px;
    font-weight: 600; font-size: 13px;
  }
  .contact-line .email { color: var(--accent-amber); }
</style>
</head>
<body>
  <main class="flyer">
    <div class="sky-artwork" role="img" aria-label="Dramatic red and orange sunset sky over a dark hillside"></div>

    <div class="brand">
      <span class="brand-dot"></span>
      <span class="brand-name">QUORVEL</span>
    </div>

    <h1 class="event-title">TAVELIN:</h1>
    <p class="event-subtitle">A FRIDAY NIGHT OF THE KINDLED WORD</p>

    <div class="scripture-band">“AND THEY PROPHESIED ALSO”</div>

    <p class="event-dates">OCTOBER 25, 2019<span class="joiner">and</span>NOVEMBER 29, 2019</p>

    <p class="venue-name">LOFTMERE COMMUNITY CENTER</p>
    <p class="venue-address">(Downtown Portland), 248 Wendlow Street<br>Portland, ME 04102</p>

    <p class="event-time">6:30PM-9:00PM</p>

    <p class="contact-line">Tel. 207-583-2914 | <span class="email">email: contact@ambervale.example</span> | web: www.quorvel.example</p>
  </main>
</body>
</html>
```